Enhance existing websites

Hello,

With my very limited web design knowledge I have designed my own websites...
Trailquote.example
Rovervalue.example

Whilst I have been very happy with the response I have received I feel the sites need enhancing. Here is what I would like to change..

1, Place a shadow around the whole pages outline so it has a 3d effect with a better background colour.

2, Improve the 'Request a valuation' tab so it stands out, maybe to also insert a curved arrow(s) to direct customer to click 'request a valuation' . Naturally this would need to be done on each page.

3, The testimonials of the 'what customers say' to change every few seconds.

4, The front page image to change every few seconds to a image of my choice.

5, any other suggestions you feel would benefit my site (obviously willing to pay extra for this and within this site)

6, given my limited knowledge my html code will surely need tidying also

7, if possible any changes not to affect my very good google ratings.

Price paid is for both sites as they're practically identical.

Thanks in advance

Glen

```html
<!DOCTYPE html>
<html lang="en">
<head>
<meta charset="utf-8">
<title>Rovervalue.example – Sell your campervan</title>
<link rel="stylesheet" href="https://fonts.googleapis.com/css2?family=Raleway:wght@400;500;600;700;800&family=Roboto:wght@400;500;700&display=swap">
<style>
:root{
  --orange:#ff8a00;
  --dark:#333333;
  --footer:#3d3d3d;
  --page-bg:#ececec;
  --panel:#f2f2f2;
  --text:#444444;
  --muted:#555555;
  --rule:#cfcfcf;
  --white:#ffffff;
}
*{box-sizing:border-box;margin:0;padding:0}
html,body{width:1066px;height:1200px;overflow:hidden}
body{position:relative;background:var(--page-bg);font-family:Arial,Helvetica,sans-serif;color:var(--text)}
.topbar{position:absolute;left:0;top:0;width:1066px;height:28px;background:var(--orange);border-bottom:3px solid var(--dark)}
.topbar__phone{position:absolute;left:98px;top:3px;color:var(--white);font-family:Roboto,Arial,sans-serif;font-size:17px;display:flex;align-items:center;gap:6px}
.topbar__phone b{font-weight:500}
.topbar__social{position:absolute;right:100px;top:7px;display:flex;gap:14px}
.topbar__social span{width:12px;height:12px;border-radius:50%;background:var(--white)}
.page{position:absolute;left:88px;top:31px;width:890px;height:1064px;background:var(--white);box-shadow:0 0 8px rgba(0,0,0,.18)}
.valuation-tab{position:absolute;left:625px;top:31px;width:441px;height:25px;background:var(--dark);color:var(--white);font-family:Raleway,sans-serif;font-size:18px;font-weight:500;padding:2px 0 0 27px;clip-path:polygon(0 0,100% 0,100% 100%,22px 100%)}
.brand{position:absolute;left:98px;top:52px}
.brand__name{font-family:Raleway,sans-serif;font-weight:700;font-size:31px;color:#444;letter-spacing:.5px}
.brand__tag{font-family:Raleway,sans-serif;font-size:15px;color:#555;margin-top:-2px}
.nav{position:absolute;top:84px;left:552px;display:flex;font-family:Raleway,sans-serif;font-size:14px;color:#444;font-weight:500}
.nav a{color:inherit;text-decoration:none;height:24px;line-height:24px}
.nav .is-active{background:var(--orange);color:var(--white);padding:0 11px;margin-right:36px}
.nav a+a{margin-right:45px}
.hero{position:absolute;left:88px;top:128px;width:890px;height:299px;background:linear-gradient(180deg,#b9c2c6 0%,#8e9a8f 40%,#6f8a52 62%,#5b6a6e 80%,#4a4e50 100%)}
.hero__title{position:absolute;left:0;width:100%;top:143px;text-align:center;font-family:Raleway,sans-serif;font-weight:800;font-size:30px;color:var(--white);text-shadow:1px 2px 3px rgba(0,0,0,.7)}
.welcome{position:absolute;left:88px;top:427px;width:890px;height:354px;background:var(--panel)}
.flag{position:absolute;left:12px;top:31px;width:230px;height:122px;background:linear-gradient(135deg,#2e3a8c 0%,#c8373d 50%,#2e3a8c 100%);border-radius:4px}
.areas__title{position:absolute;left:10px;top:159px;font-family:Raleway,sans-serif;font-weight:600;font-size:27px;color:var(--orange)}
.areas__intro{position:absolute;left:12px;top:199px;width:230px;font-size:11px;line-height:16px;color:var(--muted)}
.areas__list{position:absolute;left:12px;top:242px;display:grid;grid-template-columns:92px 83px 80px;row-gap:2.8px;font-size:11px;color:#333;line-height:15px}
.welcome__rule{position:absolute;left:269px;top:36px;width:1px;height:304px;background:var(--rule)}
.welcome__body{position:absolute;left:295px;top:38px;width:590px}
.welcome__body h1{font-family:Raleway,sans-serif;font-weight:600;font-size:28px;color:#444;margin-left:-2px;margin-bottom:10px}
.welcome__body h1 span{color:var(--orange)}
.welcome__body p{font-size:11px;line-height:16px;color:var(--muted);margin-bottom:16px;text-align:justify}
.welcome__body strong{color:#333}
.feature{position:absolute;top:830px}
.feature h2{font-family:Raleway,sans-serif;font-weight:500;font-size:19px;color:#444}
.col-how{left:103px}
.col-how h2{text-transform:uppercase;margin-top:0}
.checklist{list-style:none;margin-top:12px}
.checklist li{display:flex;align-items:center;gap:8px;height:32px;font-size:11px;color:#333}
.col-testimonials{left:402px;width:260px}
.slider-arrows{position:absolute;right:-5px;top:-2px;font-size:16px;color:#555;letter-spacing:6px}
.quote__title{font-family:Raleway,sans-serif;font-size:13px;color:#555;margin-top:13px}
.quote p{font-size:11px;line-height:16px;color:var(--muted);text-align:justify;margin-top:6px}
.quote p+p{margin-top:16px}
.col-brands{left:712px;top:825px}
.brand-grid{display:grid;grid-template-columns:repeat(7,26px);column-gap:10px;row-gap:8px;margin-top:24px}
.brand-grid span{height:24px;border-radius:3px}
.btn{position:absolute;top:1027px;height:24px;line-height:24px;padding:0 11px;background:var(--orange);color:var(--white);font-family:Raleway,sans-serif;font-weight:700;font-size:13px;border-radius:3px}
.col-rule{position:absolute;top:830px;width:1px;height:232px;background:var(--rule)}
.footer{position:absolute;left:0;top:1095px;width:1066px;height:105px;background:var(--footer);color:var(--white)}
.footer__links{position:absolute;left:100px;top:35px;font-size:11px;font-weight:bold;word-spacing:2px}
.footer__address{position:absolute;left:100px;top:58px;font-size:11px;font-weight:bold}
.footer__brand{position:absolute;left:685px;top:24px;font-family:Raleway,sans-serif;color:#8a8a8a}
.footer__brand b{display:block;font-size:31px;font-weight:700}
.footer__brand span{font-size:15px}
</style>
</head>
<body>
<div class="page"></div>

<header class="topbar">
  <div class="topbar__phone">
    <svg width="16" height="18" viewBox="0 0 16 18"><path d="M4 1c1 0 2 3 2 4s-2 1-2 2c0 2 3 6 5 6 1 0 1-2 2-2s4 1 4 2-1 4-4 4C6 17 1 10 1 5 1 2 3 1 4 1z" fill="#fff"/></svg>
    Call Us: <b>0800 123 4567</b>
  </div>
  <div class="topbar__social"><span></span><span></span><span></span></div>
</header>

<div class="valuation-tab">Request a FREE Caravan Valuation</div>

<div class="brand">
  <div class="brand__name">Rovervalue.example</div>
  <div class="brand__tag">The UK's largest buyer of campervans</div>
</div>

<nav class="nav">
  <a class="is-active">HOME</a>
  <a>HOW IT WORKS</a>
  <a>FAQ'S</a>
  <a>CONTACT US</a>
</nav>

<section class="hero" role="img" aria-label="Photo of motorhomes parked beside a fjord under misty green cliffs">
  <div class="hero__title">SELL YOUR CAMPERV QUICKLY AND SECURELY</div>
</section>

<section class="welcome">
  <div class="flag" role="img" aria-label="Waving Union flag illustration"></div>
  <h2 class="areas__title">Free Collection</h2>
  <p class="areas__intro">Below are some examples of &nbsp;of the areas we cover ...</p>
  <div class="areas__list">
    <span>Birmingham</span><span>Exeter</span><span>Manchester</span>
    <span>Cambridge</span><span>Hertford</span><span>Norwich</span>
    <span>Chelmsford</span><span>Leominster</span><span>Swansea</span>
    <span>Chichester</span><span>Lincoln</span><span>Truro</span>
    <span>Chester</span><span>Maidstone</span><span>Wakefield</span>
  </div>
  <div class="welcome__rule"></div>
  <div class="welcome__body">
    <h1>Welcome to <span>Rovervalue</span></h1>
    <p><strong>Selling your motorhome, campervan or American RV to rovervalue.example saves you the usual head-aches and costs associated with selling a vehicle,</strong> not to mention the potential risks involved. All you need to do is either call us on the freephone number provided, or click the button above and complete our online request form with details of your motorhome or campervan.</p>
    <p>We will get back to you as soon as possible with a price and a no obligation offer to buy. If you accept our offer, we'll contact you to collect your motorhome at your convenience - free of charge.</p>
    <p>It is our aim to make the process of selling your motorhome completely straightforward and hassle-free. From your initial enquiry, to having your motorhome sold with money in your bank account or cash in your hand, can take less than 24 hours. We have even managed to complete some transactions the very same day the offer was received.</p>
    <p>Remember, there are no hidden charges for our service and you are not under any obligation to accept our offer. You really do have nothing to lose by simply finding out how much we can pay for your motorhome or campervan.</p>
  </div>
</section>

<section class="feature col-how">
  <h2>How it works</h2>
  <ul class="checklist">
    <li><svg width="18" height="16" viewBox="0 0 18 16"><path d="M1 8l5 6L17 1" fill="none" stroke="#2a8a1e" stroke-width="2.5"/><path d="M1 14h12" stroke="#333" stroke-width="1"/></svg>Genuine online or verbal offer to purchase</li>
    <li><svg width="18" height="16" viewBox="0 0 18 16"><path d="M1 8l5 6L17 1" fill="none" stroke="#2a8a1e" stroke-width="2.5"/><path d="M1 14h12" stroke="#333" stroke-width="1"/></svg>Excellent prices offered and paid</li>
    <li><svg width="18" height="16" viewBox="0 0 18 16"><path d="M1 8l5 6L17 1" fill="none" stroke="#2a8a1e" stroke-width="2.5"/><path d="M1 14h12" stroke="#333" stroke-width="1"/></svg>No admin fees or hidden charges</li>
    <li><svg width="18" height="16" viewBox="0 0 18 16"><path d="M1 8l5 6L17 1" fill="none" stroke="#2a8a1e" stroke-width="2.5"/><path d="M1 14h12" stroke="#333" stroke-width="1"/></svg>Friendly professional, no hassle service</li>
    <li><svg width="18" height="16" viewBox="0 0 18 16"><path d="M1 8l5 6L17 1" fill="none" stroke="#2a8a1e" stroke-width="2.5"/><path d="M1 14h12" stroke="#333" stroke-width="1"/></svg>Instant cash or faster payment bank transfer</li>
  </ul>
</section>
<div class="col-rule" style="left:371px"></div>

<section class="feature col-testimonials">
  <h2>Testimonials</h2>
  <div class="slider-arrows">‹ ›</div>
  <div class="quote">
    <div class="quote__title">Lorem ipsum dolor sit amet</div>
    <p>Sed ut perspiciatis unde omnis iste natus error sit voluptatem accusantium doloremque laudantium, totam rem aperiam, eaque ipsa quae ab illo inventore veritatis et quasi architecto beatae vitae dicta sunt explicabo Nemo enim.</p>
    <p>odit aut fugit, sed quia consequuntur magni dolores eos qui ratione voluptatem porro .</p>
  </div>
</section>
<div class="col-rule" style="left:689px"></div>

<section class="feature col-brands">
  <h2>Selling your Campervan?</h2>
  <div class="brand-grid" aria-label="Motorhome manufacturer badges">
    <span style="background:#d33"></span><span style="background:#2f6b3a"></span><span style="background:#2a4d9a"></span><span style="background:#2b5fa8"></span><span style="background:#d43a2a"></span><span style="background:#1c8f6b"></span><span style="background:#8a96a8"></span>
    <span style="background:#e8591c"></span><span style="background:#555"></span><span style="background:#f0a020"></span><span style="background:#c62828"></span><span style="background:#d22"></span><span style="background:#c43"></span><span style="background:#3b62b8"></span>
    <span style="background:#a33;border-radius:50%"></span><span style="background:#2e66b5"></span><span style="background:#9aa"></span><span style="background:#1aa3a8"></span><span style="background:#9aa2b0"></span><span style="background:#444;border-radius:50%"></span><span style="background:#2b3f8f"></span>
    <span style="background:#6b7d95"></span><span style="background:#1d3f99"></span><span style="background:#2a6fc0"></span><span style="background:#5b7db8"></span><span style="background:#ccc"></span><span style="background:#2a3f8c"></span><span style="background:#777;border-radius:50%"></span>
    <span style="background:#c62828"></span><span style="background:#2b3f8f;border-radius:50%"></span><span style="background:#d32f2f"></span><span style="background:#c9a227"></span><span style="background:#3a88c8"></span><span style="background:#b33"></span><span style="background:#a0233a"></span>
  </div>
</section>

<div class="btn" style="left:100px">View All</div>
<div class="btn" style="left:405px">View All</div>

<footer class="footer">
  <div class="footer__links">Home &nbsp; | &nbsp; How it Works &nbsp; | &nbsp; FAQ's &nbsp; | &nbsp; Contact us</div>
  <div class="footer__address">Trailquote.example - Meadow Lane - Ashford - Kent AB1 2CD</div>
  <div class="footer__brand"><b>Rovervalue.example</b><span>The UK's largest buyer of campervans</span></div>
</footer>
</body>
</html>
```